Web re-design project for web software development agency

We need to re-design our existing website (www.tovenmedia.co.uk), and are going to start using a shorter domain (www.toven.com).
We have been in business for 8 years and it's time for an update.

We are based at Harrowmede Court (home of the code breakers). We specialise in writing software for the web. Over the years we have built up a healthy customer base and it is time to incorporate the features we build for our customers into our own site (e.g. social media).

We have a team of 8 talented developers with varied skills including: apps for mobile; complex server side software; front-end software; eCommerce software; specialised web based applications; integration software; hardware support; consultancy services. Our customers are diverse (e.g. banking; commerce; veterinary; R&D; health sector; law; accounting; film industry etc.).

Our current colour scheme is blue, white and green although we are not averse to moving away from these colours. We will also be dropping the DESIGN from our name and logo. Revised logo will be attached.

The site needs to be modern, sophisticated and leading edge. We want to show visitors to the site that we are a professional organisation.
Updates

Our logo in PSD format has been uploaded. Please drop the word DESIGN from the logo.

The deliverable for this project is a PSD (ideally we would like to see how the home page, portfolio page, resources page with mugshots, and forms are going to look).

Many thanks,
Tom

Please DO NOT include a Careers section 

We will also need a "meet our team" section with spaces for 10 photographs as well as some space underneath them so that we can add a short paragraph for each one of them.

Target Market(s)

Mainly large corporations needing bespoke web software, or generally complex projects (for anyone).

Industry/Entity Type

Software

Requirements
Must have
• We would like a home page designed that has the following elements on it:
- Show the new cookie compliance policy displayed probably in the top of the page (will disappear).
- A client Testimonial.
- Pricing icon.
- Social media Links.
- A Quote section in expand/collapse field as in (http://www.quillbrook-online.co.uk/our-services.shtml)

We would also like a portfolio page that showcases our clients in an interesting way.

Finally, we would like a form design that we can use throughout the site (i.e. how should buttons, radio buttons, checkboxes, dropdowns, text areas etc. look)?
Nice to have
• A page that follows these guidelines:
http://www.pagerivet.com/the-anatomy-of-a-perfect-landing-page

Here are a few examples of sites in our sector that we like:
- http://www.tidewell-studio.com/
- http://plinthos.co.uk/
- http://www.fernaxis.com/services/web-development (nice contact us page)
- http://www.quillbrook-online.co.uk/
- http://www.lumsa.com/
- http://www.netmoxa.co.uk/
Should not have
• No flash elemets. If anything, we will use html5.

```html
<!DOCTYPE html>
<html lang="en">
<head>
<meta charset="utf-8">
<title>TovenMedia – Home</title>
<link href="https://fonts.googleapis.com/css2?family=PT+Sans:ital,wght@0,400;0,700;1,400&family=Arimo:wght@400;700&family=Tinos:ital@1&display=swap" rel="stylesheet">
<style>
:root{
  --navy:#1d3f6e;
  --blue:#2a5a95;
  --blue-deep:#1b3d6b;
  --link:#2b62a6;
  --lime:#a7c52c;
  --lime-dark:#6f9a14;
  --page:#f0f0f0;
  --text:#555;
  --card:#fff;
  --line:#d6d6d6;
  --foot:#1e3d68;
  --foot-text:#dfe7f2;
  --foot-head:#5d93cf;
}
*{margin:0;padding:0;box-sizing:border-box}
html,body{width:1200px;height:1113px;overflow:hidden}
body{position:relative;background:var(--page);font-family:"Arimo",Arial,sans-serif;color:var(--text)}
.abs{position:absolute}
.header{left:0;top:0;width:1200px;height:155px;background:linear-gradient(#fff 0,#fff 80px,#e9e9e9 155px)}
.cookie-bar{left:299px;top:0;width:361px;height:25px;background:#4c5f77;border-radius:0 0 5px 5px;color:#e8edf3;font-family:"PT Sans",sans-serif;font-size:8px;line-height:25px;padding:0 24px 0 10px;white-space:nowrap}
.cookie-bar u{color:#fff}
.cookie-close{position:absolute;right:8px;top:6px;width:13px;height:13px;border-radius:50%;background:#fff;color:#4c5f77;font-size:10px;line-height:13px;text-align:center;font-weight:700}
.contact-top{right:270px;top:10px;text-align:right;color:var(--link);font-family:"PT Sans",sans-serif;white-space:nowrap}
.contact-top .phone{font-size:13.5px;letter-spacing:.5px;line-height:16px}
.contact-top .mail{font-size:9px;margin-top:2px;line-height:12px}
.icon-phone{left:938px;top:13px}
.icon-mail{left:937px;top:29px}
.brand{left:276px;top:93px;display:flex;align-items:flex-end;gap:8px}
.brand-mark{width:22px;height:22px;background:var(--lime)}
.brand-name{font-family:"PT Sans",sans-serif;font-weight:700;font-size:27px;color:var(--navy);letter-spacing:.5px;line-height:1}
.nav{left:520px;top:131px;display:flex;gap:4px;font-family:"PT Sans",sans-serif;font-size:11px;color:var(--navy);letter-spacing:.2px;white-space:nowrap}
.nav a{color:inherit;text-decoration:none;padding:2px 4px}
.nav a.active{background:var(--blue);color:#fff;border-radius:3px}
.hero{left:0;top:155px;width:1200px;height:237px;background:radial-gradient(ellipse 400px 200px at 780px 100px,#3a6aa5,transparent),linear-gradient(#2f5f9c,#224c83 170px,#1d4478 170px,#1e4579)}
.hero::after{content:"";position:absolute;left:0;bottom:-6px;width:100%;height:6px;background:linear-gradient(#c9c9c9,var(--page))}
.hero-title{left:290px;top:177px;font-family:"PT Sans",sans-serif;font-weight:400;font-size:20px;color:#fff}
.hero-copy{left:290px;top:212px;width:265px;font-family:"PT Sans",sans-serif;font-size:10.5px;line-height:13px;color:#d6e2f1}
.cta{left:290px;top:265px;width:162px;height:28px;border-radius:4px;background:linear-gradient(#8dc02a,#5f9612);color:#fff;font-family:"PT Sans",sans-serif;font-weight:700;font-size:11.5px;line-height:28px;padding-left:43px;box-shadow:0 1px 2px rgba(0,0,0,.3)}
.cta svg{position:absolute;left:14px;top:8px}
.showcase-back2{left:622px;top:215px;width:60px;height:118px;background:linear-gradient(#e9eef6,#b8c8dc);border-radius:3px;box-shadow:0 2px 6px rgba(0,0,0,.35)}
.showcase-back1{left:656px;top:202px;width:60px;height:138px;background:linear-gradient(#f4efe2,#d9c8a3);border-radius:3px;box-shadow:0 2px 6px rgba(0,0,0,.35)}
.showcase-main{left:692px;top:173px;width:237px;height:196px;background:linear-gradient(120deg,#fafcf7 0,#eef5e4 45%,#c8d9ea 78%,#3f6fb0 88%);border-radius:3px;box-shadow:0 3px 10px rgba(0,0,0,.4)}
.card{top:430px;width:211px;height:124px;background:var(--card);box-shadow:0 0 2px rgba(0,0,0,.12)}
.card h2{position:absolute;left:8px;top:10px;font-family:"PT Sans",sans-serif;font-weight:400;font-size:14.5px;color:var(--link)}
.card-1{left:273px}.card-2{left:497px;background:linear-gradient(#f1f1f1,#fff 40px)}.card-3{left:721px}
.project-thumb{position:absolute;left:7px;top:34px;width:80px;height:60px;border:1px solid #e2e2e2;border-radius:5px;background:#fff;display:flex;align-items:center;justify-content:center;font-family:"PT Sans",sans-serif;font-weight:700;font-size:11px;color:var(--link);text-align:center;line-height:12px}
.project-name{position:absolute;left:99px;top:35px;font-family:"PT Sans",sans-serif;font-size:11px;color:var(--link)}
.project-text{position:absolute;left:99px;top:52px;width:100px;font-size:8.5px;line-height:10.5px;color:#777}
.card-3 h2{left:26px}
.quote-text{position:absolute;left:28px;top:36px;width:172px;font-size:8.5px;line-height:10.5px;color:#777}
.rule{left:272px;width:660px;height:1px;background:var(--line)}
.label{height:29px;line-height:29px;text-align:center;font-family:"PT Sans",sans-serif;font-size:12px;color:var(--link);background:repeating-linear-gradient(135deg,#e2e2e2 0 2px,#ececec 2px 4px)}
.label-customers{left:547px;top:608px;width:109px}
.label-talked{left:523px;top:748px;width:157px;font-style:italic}
.arrow-btn{top:670px;width:18px;height:18px;border-radius:50%;background:#c7c7c7;border:2px solid #e2e2e2}
.arrow-btn svg{display:block;margin:3px auto}
.customer{top:658px;height:41px;display:flex;align-items:center;justify-content:center;font-family:"PT Sans",sans-serif;font-weight:700;font-size:18px;white-space:nowrap}
.c1{left:298px;width:139px;background:#fff;color:#8a6c2c}
.c2{left:454px;width:154px;background:#fff;color:#333}
.c3{left:624px;width:111px;background:#fff;color:#17796d;font-size:10.5px}
.c4{left:752px;width:155px;background:#0d0d0d;color:#fff}
.testimonial{top:797px;width:186px;font-size:8.8px;line-height:12.3px;color:#555;text-align:justify}
.testimonial cite{display:block;margin-top:12px;font-family:"Tinos",serif;font-size:10px;color:#666}
.t1{left:272px}.t2{left:509px}.t3{left:744px}
.footer{left:0;top:931px;width:1200px;height:150px;background:linear-gradient(#1f3f6c,#17345c)}
.foot-divider{top:946px;width:1px;height:118px;background:#2e5487}
.foot-col{top:946px;font-size:8.8px;color:var(--foot-text);line-height:16.5px}
.foot-col h3{font-family:"PT Sans",sans-serif;font-weight:400;font-size:10px;color:var(--foot-head);margin-bottom:5px;letter-spacing:.3px}
.foot-col strong{font-size:10px;letter-spacing:.4px}
.foot-col .addr{line-height:13.5px}
.foot-col .lbl{color:var(--lime);font-weight:700}
.social{display:flex;gap:5px;margin-top:4px}
.social span{width:20px;height:20px;border-radius:3px;background:#5d86bb}
.foot-brand{left:764px;top:1022px;display:flex;align-items:flex-end;gap:7px}
.foot-brand .brand-mark{width:18px;height:18px}
.foot-brand .brand-name{font-size:20px;color:#fff;font-weight:400}
.bottom-bar{left:0;top:1080px;width:1200px;height:33px;background:linear-gradient(#08101c,#000);color:#ddd;font-size:8.8px;text-align:center;line-height:33px}
.bottom-bar b{color:#fff}
</style>
</head>
<body>
<div class="abs header"></div>
<div class="abs cookie-bar">We are committed to protecting your personal information. <u>click here</u> for our privacy and policy.<span class="cookie-close">×</span></div>
<div class="abs contact-top"><div class="phone">1800 555 019</div><div class="mail">info@tovenmedia.co.uk</div></div>
<svg class="abs icon-phone" width="13" height="10" viewBox="0 0 13 10"><path d="M1 3 Q6.5 -1 12 3 L10 4 L9 2.5 L4 2.5 L3 4 Z" fill="#2b62a6"/><rect x="3" y="5" width="7" height="5" rx="1" fill="#2b62a6"/></svg>
<svg class="abs icon-mail" width="15" height="10" viewBox="0 0 15 10"><rect width="15" height="10" fill="#2b62a6"/><path d="M0 0 L7.5 6 L15 0" stroke="#fff" fill="none"/></svg>

<div class="abs brand"><span class="brand-mark"></span><span class="brand-name">TOVENMEDIA</span></div>
<nav class="abs nav"><a class="active">HOME</a><a>ABOUT US</a><a>OUR SERVICES</a><a>TECHNOLOGY</a><a>PORTFOLIO</a><a>CONTACT US</a></nav>

<section class="abs hero"></section>
<h1 class="abs hero-title">be the brand experience</h1>
<p class="abs hero-copy">The company is in a growth phase taking on projects of ever increasing complexity while still welcoming smaller projects more efficiently and effectively.</p>
<div class="abs cta"><svg width="16" height="12" viewBox="0 0 16 12"><rect width="16" height="12" rx="2" fill="#fff"/><path d="M3 6 H11 M8 3 L11 6 L8 9" stroke="#5f9612" stroke-width="2" fill="none"/></svg>GET STARTED NOW</div>
<div class="abs showcase-back2" role="img" aria-label="Screenshot of a client website"></div>
<div class="abs showcase-back1" role="img" aria-label="Screenshot of a client website"></div>
<div class="abs showcase-main" role="img" aria-label="Screenshot of a veterinary client website with a vet holding a cat"></div>

<div class="abs card card-1"><h2>Recent Projects</h2><div class="project-thumb">Brightpaw<br>Vets</div><div class="project-name">Brightpaw Vets</div><p class="project-text">We developed a fully customizable football club website system. New sites can be many</p></div>
<div class="abs card card-2"></div>
<div class="abs card card-3"><h2>Get a Quote Today</h2><p class="quote-text">Contrary to popular belief, Lorem Ipsum is not simply random text. It has roots in a piece of classical Latin literature from 45 BC, making it over 2000 years old</p></div>

<div class="abs rule" style="top:587px"></div>
<div class="abs label label-customers">OUR CUSTOMERS</div>
<div class="abs arrow-btn" style="left:274px"><svg width="8" height="10" viewBox="0 0 8 10"><path d="M6 1 L2 5 L6 9" stroke="#fff" stroke-width="2" fill="none"/></svg></div>
<div class="abs customer c1">Aurumvault</div>
<div class="abs customer c2">LEDGERLINE</div>
<div class="abs customer c3">Corvane Animal Health</div>
<div class="abs customer c4">QUICKRAIL</div>
<div class="abs arrow-btn" style="left:912px"><svg width="8" height="10" viewBox="0 0 8 10"><path d="M2 1 L6 5 L2 9" stroke="#fff" stroke-width="2" fill="none"/></svg></div>

<div class="abs rule" style="top:725px"></div>
<div class="abs label label-talked">AS TALKED ABOUT BY</div>
<blockquote class="abs testimonial t1">“Curabitu et justo est, nec pellentesque tupis. Suspendisse vel lorem nec purun sutrum con-dimentum. Conec malesuada orci eu ligula gravida molestie.<cite>Dean Hollis, Alder Fund</cite></blockquote>
<blockquote class="abs testimonial t2">“Curabitu et justo est, nec pellentesque tupis. Suspendisse vel lorem nec purun sutrum con-dimentum. Conec malesuada orci eu ligula gravida molestie.<cite>Mark Tenby, Larkspur Capital</cite></blockquote>
<blockquote class="abs testimonial t3">“Curabitu et justo est, nec pellentesque tupis. Suspendisse vel lorem nec purun sutrum con-dimentum. Conec malesuada orci eu ligula gravida molestie.<cite>Paul Weston, Quorum Capital</cite></blockquote>

<footer class="abs footer"></footer>
<div class="abs foot-divider" style="left:440px"></div>
<div class="abs foot-divider" style="left:591px"></div>
<div class="abs foot-divider" style="left:727px"></div>
<div class="abs foot-col" style="left:288px"><h3>CONTACT US</h3><strong>TOVEN MEDIA</strong><div class="addr">Suite EU3/4<br>Science and Innovation Center<br>Harrowmede Court</div><div style="margin-top:6px"><span class="lbl">T:</span> 01632 960 450</div><div><span class="lbl">E:</span> info@tovenmedia.co.uk</div></div>
<div class="abs foot-col" style="left:480px"><h3>RESEACH</h3>Design<br>Development<br>Project management<br>IT Solutions<br>Ongoing Support</div>
<div class="abs foot-col" style="left:625px"><h3>ABOUT US</h3>Contact<br>Terms of Use<br>Privacy Policy<br>Fair Information</div>
<div class="abs foot-col" style="left:762px"><h3>CONNECT WITH US</h3><div class="social"><span></span><span></span><span></span><span></span></div></div>
<div class="abs foot-brand"><span class="brand-mark"></span><span class="brand-name">TOVENMEDIA</span></div>
<div class="abs bottom-bar">© 2009 - 2011 <b>TovenMedia.</b> All Rights Reserved.</div>
</body>
</html>
```